Mirelle "Glass Tide" single cover

We need a cover for Mirelle's New upcoming single "Glass Tide"
We have posted some Pictures and logo that we want you to work With. We need you to get her to look good :).The title is "Glass Tide" and is "Mirelle feat. Tovro pip rascal"
The songs is a little hiphop/RnB (Norah K'ish).
You can choose what colour you want for the logo and overall. But we don't want it to be gloomy.
watch www.mirelle-example.no or www.sociabook.example/mirellemusic
This is a digital release so we need only front page 12x12cm
Updates
If anyone wants to remove the background from the pictures and be creative that is fine! :)
Industry/Entity Type
Digital
Colors
Designer to choose colors to be used in the design.
Look and feel
Each slider illustrates characteristics of the customer's brand and the style your logo design should communicate.

```html
<!DOCTYPE html>
<html lang="en">
<head>
<meta charset="utf-8">
<title>Mirelle – Glass Tide single cover</title>
<link href="https://fonts.googleapis.com/css2?family=Open+Sans:wght@400;600&family=Yesteryear&display=swap" rel="stylesheet">
<style>
  :root {
    --page: #ffffff;
    --brick: #b8492c;
    --brick-light: #d9714a;
    --mortar: #8fb4d0;
    --jacket: #141414;
    --hair: #7a4a2a;
    --ink: #ffffff;
  }
  html, body {
    margin: 0;
    padding: 0;
    width: 1200px;
    height: 1000px;
    overflow: hidden;
    background: var(--page);
  }
  .canvas {
    position: relative;
    width: 1200px;
    height: 1000px;
    background: var(--page);
  }
  .cover {
    position: absolute;
    left: 125px;
    top: 28px;
    width: 942px;
    height: 942px;
    overflow: hidden;
  }
  .cover-photo {
    position: absolute;
    inset: 0;
    background:
      radial-gradient(ellipse 40% 55% at 35% 70%, var(--jacket) 0%, rgba(20,20,20,0.85) 55%, rgba(20,20,20,0) 100%),
      radial-gradient(ellipse 30% 35% at 30% 35%, var(--hair) 0%, rgba(122,74,42,0) 100%),
      linear-gradient(115deg, var(--brick) 0%, var(--brick-light) 55%, var(--mortar) 80%, var(--brick) 100%);
  }
  .artist-name {
    position: absolute;
    right: 46px;
    top: 62px;
    margin: 0;
    font-family: "Open Sans", sans-serif;
    font-weight: 600;
    font-size: 64px;
    letter-spacing: 2px;
    color: var(--ink);
    line-height: 1;
  }
  .single-title {
    position: absolute;
    left: 60px;
    top: 625px;
    margin: 0;
    font-family: "Yesteryear", cursive;
    font-weight: 400;
    font-size: 196px;
    line-height: 1;
    color: var(--ink);
    white-space: nowrap;
  }
  .featuring {
    position: absolute;
    left: 466px;
    top: 872px;
    margin: 0;
    font-family: "Open Sans", sans-serif;
    font-weight: 400;
    font-size: 31px;
    color: var(--ink);
    white-space: nowrap;
  }
</style>
</head>
<body>
  <main class="canvas">
    <section class="cover">
      <div class="cover-photo" role="img" aria-label="Photo of the singer with long curly hair and a black leather jacket leaning against a red brick wall"></div>
      <p class="artist-name">Mirelle</p>
      <h1 class="single-title">Glass Tide</h1>
      <p class="featuring">ft. Tovro pip rascal</p>
    </section>
  </main>
</body>
</html>
```